Skill Up Salary Up

Full Page
7.5 w x 10 h / 8 w x 10.75 h + .25" bleed
Full-Page Career Course Ad
Project Overview
• Goal: Create a visually attractive, modern, and uncluttered full-page magazine advertisement to list available career courses.
• Tone: Creative, professional, and attention-grabbing to prevent the reader from turning the page. The final design must prioritize readability.

Content Requirements
1. Header/Headline: Must be the primary focus. And grab peoples attention
2. Course Listing: A clear, well-organized list of the career courses.
________________________________________
Design & Aesthetic Directives
1. Layout & Readability (Crucial)
• The final ad must not look crowded or busy.
• Prioritize white space to make the text "breathe" and ensure the course list is easy to scan and read.
• Use a modern, clean, and professional typeface (font choice is critical for the aesthetic).
2. Visual Style
• Aim for a creative, modern, and fresh look. Avoid outdated or generic stock imagery/layouts.
3. Imagery/Graphic Element (Artist's Choice)
You have creative freedom regarding the main graphic element.
• Option A (Photography): Use a photo of a white male American with a collared shirt. The imagery should convey success, focus, or professional development.
• Option B (Vector/Illustration): Use a modern vector graphic, illustration, or abstract design. This could be used to symbolize growth, connection, or a career path.
The choice of graphic element is yours, but it must support the overall modern and uncrowded aesthetic.

Requirements
Must have
• Partial listing .. is part of the Vocational Horizon Course

```html
<!DOCTYPE html>
<html lang="en">
<head>
<meta charset="utf-8">
<title>Skill Up, Salary Up – Upcoming NVX Courses</title>
<link href="https://fonts.googleapis.com/css2?family=Poppins:ital,wght@0,500;0,600;0,700;0,800;0,900;1,500&family=Lexend:wght@300;400&display=swap" rel="stylesheet">
<style>
  :root{
    --navy:#2e2d82;
    --ink:#1f1f3a;
    --body:#3a3a4a;
    --cream:#ecd9c8;
    --paper:#ffffff;
    --peach:#f4b486;
    --mist:#e7e9f4;
  }
  *{margin:0;padding:0;box-sizing:border-box}
  html,body{width:900px;height:1200px;overflow:hidden;background:var(--paper)}
  .ad{position:relative;width:900px;height:1200px;overflow:hidden;background:var(--paper);font-family:'Lexend',sans-serif;color:var(--body)}
  .hero-art{position:absolute;left:230px;top:0;width:670px;height:356px;
    background:linear-gradient(100deg,var(--mist) 0%,#eef0f7 35%,#f6c9a5 62%,var(--peach) 100%)}
  .headline{position:absolute;left:48px;top:28px;font-family:'Poppins',sans-serif;font-weight:900;
    font-size:74px;line-height:70px;letter-spacing:-1px;color:var(--navy);z-index:2}
  .top-band{position:absolute;left:0;top:354px;width:900px;height:38px;background:var(--navy);z-index:1}
  .promo-box{position:absolute;left:48px;top:185px;width:240px;height:207px;background:var(--navy);
    border-radius:30px 30px 0 0;padding:22px 0 0 16px;font-family:'Poppins',sans-serif;z-index:2}
  .promo-box .upcoming{color:#fff;font-weight:900;font-size:37px;line-height:40px;letter-spacing:-.5px}
  .promo-box .courses{color:#fff;font-weight:900;font-size:29px;line-height:36px;letter-spacing:-.5px;margin-bottom:6px}
  .promo-box .perk{color:var(--cream);font-weight:700;font-size:16px;line-height:26px;white-space:nowrap}
  .course-icon{position:absolute}
  .course-title{position:absolute;height:25px;background:var(--navy);color:#fff;font-family:'Poppins',sans-serif;
    font-weight:600;font-size:19px;line-height:25px;padding-left:10px;white-space:nowrap;overflow:hidden}
  .course-title.long{font-size:18px;letter-spacing:-.2px}
  .tagline{position:absolute;font-family:'Poppins',sans-serif;font-style:italic;font-weight:500;font-size:16px;line-height:18px;color:var(--ink);white-space:nowrap}
  .list{position:absolute;list-style:none;font-weight:300;font-size:16px;color:var(--body)}
  .list li{position:relative;padding-left:27px;white-space:nowrap}
  .list li::before{content:"•";position:absolute;left:0;font-size:12px}
  .note{position:absolute;font-weight:300;font-size:16px;line-height:20px;color:var(--body);white-space:nowrap}
  .label{position:absolute;font-family:'Poppins',sans-serif;font-weight:600;font-size:15px;color:var(--ink)}
  .schedule{position:absolute;font-family:'Poppins',sans-serif;font-weight:700;font-size:15.5px;color:var(--navy);white-space:nowrap}
  .bottom-band{position:absolute;left:0;top:1089px;width:900px;height:111px;background:var(--navy)}
  .seal{position:absolute;left:53px;top:1022px;width:148px;height:148px;border-radius:50%;background:var(--navy);border:3px solid #fff}
</style>
</head>
<body>
<div class="ad">

  <div class="hero-art" role="img" aria-label="Illustration of a man in a blue collared sweater at a desk, pointing a pen at growth charts on a laptop, with a whiteboard and a warm city skyline window behind him"></div>

  <h1 class="headline">SKILL UP,<br>SALARY UP</h1>

  <div class="top-band"></div>
  <div class="promo-box">
    <div class="upcoming">UPCOMING</div>
    <div class="courses">NVX COURSES</div>
    <div class="perk">MEN &amp; WOMEN</div>
    <div class="perk">IN-PERSON &amp; REMOTE</div>
    <div class="perk">PARTIAL SCHOLARSHIPS</div>
  </div>

  <!-- Vocational Horizon -->
  <svg class="course-icon" style="left:38px;top:424px" width="54" height="54" viewBox="0 0 54 54" fill="none" stroke="var(--navy)" stroke-width="2" stroke-linecap="round">
    <path d="M30 30 L50 8 M40 6 h10 v10"/><path d="M14 30 l10 -10 l12 12 l-10 10 z"/><path d="M10 44 l8 -8 M20 50 l12 -10"/>
    <path d="M6 20 l4 2 M8 12 l4 4 M16 6 l2 4 M24 4 v4"/>
  </svg>
  <div class="course-title" style="left:95px;top:420px;width:309px">Vocational Horizon</div>
  <div class="tagline" style="left:104px;top:448px">Business Skills &amp; Knowledge to:</div>
  <ul class="list" style="left:104px;top:467px;line-height:18.2px">
    <li>Impress your interviewer</li>
    <li>Maximize Income</li>
    <li>Start / Run Your Business</li>
  </ul>
  <div class="label" style="left:104px;top:525px">PARTIAL LISTING</div>
  <ul class="list" style="left:99px;top:547px;line-height:21.2px">
    <li>Computers</li><li>Marketing</li><li>Sales</li><li>Finance</li><li>Healthcare</li>
    <li style="line-height:18px;padding-top:2px">Business<br>Strategy</li>
  </ul>
  <ul class="list" style="left:259px;top:547px;line-height:21.2px">
    <li>Communication</li><li>LedgerBooks</li><li>Investments</li><li>Real Estate</li><li>Accounting</li>
  </ul>
  <div class="schedule" style="left:100px;top:703px">4-5 MONTHS | NOV&nbsp; 2025</div>

  <!-- Software -->
  <svg class="course-icon" style="left:38px;top:782px" width="54" height="52" viewBox="0 0 54 52" fill="none" stroke="var(--navy)" stroke-width="2" stroke-linecap="round">
    <rect x="2" y="2" width="50" height="44"/><rect x="6" y="6" width="42" height="36"/>
    <circle cx="26" cy="20" r="8"/><path d="M22 28 v10 M30 28 v10 M22 34 h8"/><path d="M2 46 l4 4 h8"/>
  </svg>
  <div class="course-title" style="left:95px;top:780px;width:309px">Software, Web &amp; Apps</div>
  <div class="tagline" style="left:108px;top:807px"># 2 Best Tech Job</div>
  <div class="tagline" style="left:104px;top:825px">National Career Review 2025</div>
  <div class="note" style="left:108px;top:847px">Job Opportunities</div>
  <ul class="list" style="left:104px;top:868px;line-height:21.2px">
    <li>Computer Programmer</li><li>Software Developer/Mobile</li><li>Engineer Developer (Apps)</li>
  </ul>
  <div class="label" style="left:104px;top:934px;font-size:16px">Optional:</div>
  <div class="note" style="left:104px;top:953px">Bachelors in Prog. &amp; Tech.</div>
  <div class="schedule" style="left:101px;top:975px">NOV&nbsp; 2025</div>

  <!-- Bookkeeping -->
  <svg class="course-icon" style="left:482px;top:424px" width="54" height="52" viewBox="0 0 54 52" fill="none" stroke="var(--navy)" stroke-width="2" stroke-linecap="round">
    <circle cx="26" cy="14" r="11"/><circle cx="26" cy="14" r="6"/><path d="M26 25 v8"/>
    <path d="M18 34 h14 v14 h-14 z M32 42 h18"/><path d="M4 30 v6 M4 40 v2 M8 30 v6 M8 40 v2"/><path d="M38 20 h8 v10"/>
  </svg>
  <div class="course-title" style="left:545px;top:420px;width:325px">Bookkeeping LedgerBooks</div>
  <div class="tagline" style="left:557px;top:448px">Train for a quality job</div>
  <div class="tagline" style="left:557px;top:466px">Manage your own books</div>
  <ul class="list" style="left:556px;top:486px;line-height:21.2px">
    <li>Finance Management</li><li>Customer &amp; Vendor Mgmt.</li><li>Advanced Tools</li>
  </ul>
  <div class="schedule" style="left:558px;top:556px">5 WEEKS |&nbsp; NOV&nbsp; 2025</div>

  <!-- IT -->
  <svg class="course-icon" style="left:483px;top:622px" width="54" height="54" viewBox="0 0 54 54" fill="none" stroke="var(--navy)" stroke-width="2" stroke-linecap="round">
    <path d="M12 18 a8 8 0 0 1 10 -8 a10 10 0 0 1 18 4 a6 6 0 0 1 6 6"/>
    <rect x="4" y="20" width="46" height="26" rx="4"/><rect x="12" y="26" width="30" height="14"/>
    <path d="M16 31 h22 M16 35 h14 M2 50 h50"/>
  </svg>
  <div class="course-title long" style="left:545px;top:620px;width:325px">IT Desktop &amp; Networking Support</div>
  <div class="tagline" style="left:562px;top:647px">#2 Best Job</div>
  <div class="tagline" style="left:558px;top:665px">National Career Review 2025</div>
  <div class="note" style="left:557px;top:689px">Masters IT:</div>
  <ul class="list" style="left:557px;top:710px;line-height:21px">
    <li>Desktop OS</li><li>Networks</li><li>Servers</li><li>Cloud</li>
  </ul>
  <div class="schedule" style="left:558px;top:805px">7 MONTHS | Dec 2025</div>

  <!-- Office suite -->
  <svg class="course-icon" style="left:481px;top:866px" width="52" height="54" viewBox="0 0 52 54" fill="none" stroke="var(--navy)" stroke-width="2">
    <rect x="6" y="6" width="40" height="42"/>
  </svg>
  <div class="course-title" style="left:545px;top:864px;width:325px;padding-left:16px">Officeline Suite- Computers</div>
  <div class="tagline" style="left:557px;top:890px">The New&nbsp;&nbsp; Job Prerequisite</div>
  <ul class="list" style="left:556px;top:911px;line-height:21.2px">
    <li>Gridsheet</li><li>Writer</li><li>Mailbox</li><li>Slidedeck</li>
  </ul>
  <div class="note" style="left:557px;top:994px">Computer lab available to practice</div>
  <div class="schedule" style="left:555px;top:1025px">5 WEEKS | DEC 2025</div>

  <div class="bottom-band"></div>
  <div class="seal"></div>
</div>
</body>
</html>
```